2 Labels Pet Treat Label Hemp Extract "Dogs and Cats"

We are currently looking for an "easy on the eye" type of pet treat label. Our colors are mostly Black and Gold however, we are open to suggestions. First label is your normal "Hemp Extract Pet Treat". Second label is "Hemp Extract for Pain & Inflammation plus calming" We would like to work with you on inputting the small details. Please use buzzwords such as Veterinary recommended etc. We would like our Logo on there as well if possible. Please make room for Ingredient list as well. A search on google for Pet treats CBD... or in this case "Hemp Extract" that should give you some idea of what we are looking for. I normally use Canva however, if you can show us how to make edits for future use, we would appreciate that.. FYI. It's 30 dog treats in a bag. 5mg of Hemp Extract. Totaling 150mg of Hemp Extract.
The 2 Logos should only be different in color since one is for Pain and Inflamation plus calming. and the other is just hemp extract.

Target Market(s)

Dogs & Cats

Font styles to use
Decorative
Script
Other font styles liked:
• Bebas Nuee

Requirements
Must have
• Must Say Hemp Extract and not CBD. Must have 5mg of Hemp Extract. Must have a few buzz words such as Veterinarian recommended, Must say Grain Free. No Dairy.
• The label needs to be on a 3" x 4.5" Sticker. So essentially the label is just a sticker vs the whole bag.
• The sticker will go a brown kraft bag, but the label for this project will be on a 3" x 4.5" Sticker.
Should not have
• CBD

```html
<!DOCTYPE html>
<html lang="en">
<head>
<meta charset="utf-8">
<title>Marrowby Hemp Extract Pet Treat</title>
<link href="https://fonts.googleapis.com/css2?family=Bebas+Neue&family=Oswald:wght@500;600&family=Montserrat:wght@500;600;700;800&display=swap" rel="stylesheet">
<style>
  :root {
    --bg: #a9b8c3;
    --cream: #f0eacb;
    --cream-light: #f6f1d8;
    --green: #a7af3d;
    --ink: #2a2e1f;
    --blue: #1b8fc7;
    --blue-deep: #0f5f8c;
    --tan: #d9b47e;
    --brown: #7c5230;
  }
  * { margin: 0; padding: 0; box-sizing: border-box; }
  html, body { width: 1200px; height: 1141px; overflow: hidden; }
  body { background: var(--bg); position: relative; font-family: "Montserrat", sans-serif; }

  .pouch-face {
    position: absolute; left: 297px; top: 42px;
    width: 605px; height: 1056px;
    background: var(--cream);
    border-radius: 10px;
    overflow: hidden;
  }
  .swoosh { position: absolute; inset: 0; width: 100%; height: 100%; }

  .brand {
    position: absolute; top: 225px; left: 0; width: 100%;
    text-align: center; color: var(--ink);
  }
  .brand-mark {
    display: inline-block; width: 14px; height: 14px; border-radius: 50%;
    background: var(--ink); vertical-align: middle; margin-right: 10px;
  }
  .brand-name {
    font-family: "Oswald", sans-serif; font-weight: 600;
    font-size: 40px; letter-spacing: 8px; vertical-align: middle;
  }
  .brand-sub {
    font-family: "Oswald", sans-serif; font-weight: 500;
    font-size: 11px; letter-spacing: 5px; margin-top: 6px;
  }

  .kicker {
    position: absolute; top: 368px; left: 0; width: 100%;
    text-align: center;
    font-family: "Oswald", sans-serif; font-weight: 600;
    font-size: 42px; line-height: 1.1; color: var(--ink);
  }
  .product-title {
    position: absolute; top: 424px; left: 108px;
    font-family: "Bebas Neue", sans-serif;
    font-size: 118px; line-height: 1; color: var(--blue);
    -webkit-text-stroke: 1px var(--blue-deep);
  }

  .photo-dog {
    position: absolute; left: 50px; top: 672px;
    width: 235px; height: 190px; border-radius: 14px;
    background: linear-gradient(160deg, #2b2b2b 0%, #454140 60%, #e8e4de 100%);
    opacity: 0.9;
  }
  .photo-treats {
    position: absolute; left: 330px; top: 560px;
    width: 180px; height: 300px; border-radius: 14px;
    background: linear-gradient(130deg, var(--tan) 0%, #c99a62 60%, var(--brown) 100%);
    opacity: 0.9;
  }

  .dose {
    position: absolute; left: 118px; top: 562px; color: var(--ink);
  }
  .dose-amount { font-size: 36px; font-weight: 800; line-height: 1; }
  .dose-label { font-size: 19px; font-weight: 700; margin-top: 4px; line-height: 1.1; }
  .dose-per { font-size: 14px; font-weight: 600; margin-top: 4px; line-height: 1.1; }

  .facts {
    position: absolute; left: 96px; top: 872px;
    width: 412px; height: 132px;
    border: 2px solid var(--ink); border-radius: 14px;
    display: grid; grid-template-columns: 113px 134px 1fr;
    color: var(--ink);
  }
  .facts > div { display: flex; flex-direction: column; justify-content: center; align-items: center; }
  .facts > div + div { border-left: 2px solid var(--ink); }
  .count { font-size: 26px; font-weight: 800; }
  .count small { font-size: 17px; }
  .free { text-align: center; line-height: 1; }
  .free + .free { margin-top: 12px; }
  .free span { display: block; font-size: 15px; font-weight: 800; }
  .free strong { display: block; font-size: 24px; font-weight: 800; }
  .facts-right { padding: 0 !important; }
  .claim {
    flex: 1; width: 100%; display: flex; align-items: center; justify-content: center;
    font-size: 15px; font-weight: 800; line-height: 1.05; text-align: center;
    border-bottom: 2px solid var(--ink);
  }
  .weight { flex: 1; width: 100%; display: flex; align-items: center; justify-content: center; gap: 10px; }
  .weight-label { font-size: 14px; font-weight: 600; line-height: 1; }
  .weight-value { font-size: 28px; font-weight: 800; }

  .ingredients {
    position: absolute; left: 96px; top: 1012px; width: 412px;
    font-size: 10px; font-weight: 500; line-height: 1.3; color: var(--ink);
    text-align: center;
  }
  .ingredients strong { font-weight: 800; }
</style>
</head>
<body>
  <main class="pouch-face">
    <svg class="swoosh" viewBox="0 0 605 1056" preserveAspectRatio="none" aria-hidden="true">
      <defs>
        <linearGradient id="greenFill" x1="0" y1="0" x2="0" y2="1">
          <stop offset="0" stop-color="#b4bb4a"/>
          <stop offset="1" stop-color="#9aa634"/>
        </linearGradient>
      </defs>
      <path d="M0 1056 L0 990 C160 810 380 450 605 235 L605 1056 Z" fill="#f6f1d8"/>
      <path d="M0 1056 L30 1056 C190 860 400 500 605 290 L605 1056 Z" fill="url(#greenFill)"/>
    </svg>

    <header class="brand">
      <div><span class="brand-mark"></span><span class="brand-name">MARROWBY</span></div>
      <div class="brand-sub">HEMP EXTRACTS</div>
    </header>

    <p class="kicker">HEMP EXTRACT</p>
    <h1 class="product-title">PET TREAT</h1>

    <div class="photo-dog" role="img" aria-label="Photo of a black and white dog playing"></div>
    <div class="photo-treats" role="img" aria-label="Photo of a pile of bone-shaped treats"></div>

    <div class="dose">
      <div class="dose-amount">150mg</div>
      <div class="dose-label">of Hemp Extract</div>
      <div class="dose-per">5mg per treat</div>
    </div>

    <section class="facts">
      <div><span class="count">30<small>PCS</small></span></div>
      <div>
        <p class="free"><span>GRAIN</span><strong>FREE</strong></p>
        <p class="free"><span>DAIRY</span><strong>FREE</strong></p>
      </div>
      <div class="facts-right">
        <p class="claim">VETERINARIAN<br>RECOMMENDED</p>
        <p class="weight"><span class="weight-label">NET<br>WEIGHT</span><span class="weight-value">150g</span></p>
      </div>
    </section>

    <p class="ingredients"><strong>INGREDIENTS:</strong> Sweet potato, chickpea flour, peanut butter, coconut oil, pumpkin, hemp extract, rosemary extract.</p>
  </main>
</body>
</html>
```